Copper Lantern Advisory: Ebook Project Cover Design Needed

I recently finished writing Copper Lantern Advisory and I need the front cover and back cover for the ebook.

I'm looking for people to want to open it based on the cover online, as I won't sell it in traditional bookstores. I'd like the ebook cover, as well as for the physical book in the 6x9 format.

```html
<!DOCTYPE html>
<html lang="en">
<head>
<meta charset="utf-8">
<title>Copper Lantern Advisory – Book Cover</title>
<link rel="stylesheet" href="https://fonts.googleapis.com/css2?family=Bebas+Neue&family=Montserrat:wght@600&display=swap">
<style>
  :root {
    --stage: #2a2a2a;
    --paper: #ffffff;
    --night: #141417;
    --night-warm: #2b231e;
    --copper: #f5a222;
    --teal: #3b8a7f;
    --ink-light: #ffffff;
    --money-green: #3f7f72;
    --money-gold: #9b7a4a;
  }
  * { box-sizing: border-box; margin: 0; padding: 0; }
  html, body {
    width: 1200px;
    height: 905px;
    overflow: hidden;
    background: var(--stage);
  }
  .cover {
    position: absolute;
    left: 313px;
    top: 22px;
    width: 574px;
    height: 861px;
    background: linear-gradient(180deg, var(--night) 0%, var(--night-warm) 100%);
    overflow: hidden;
  }
  .cover__top {
    position: absolute;
    left: 0; top: 0;
    width: 100%;
    height: 285px;
    background: var(--paper);
  }
  .title {
    position: absolute;
    left: 54px;
    top: 58px;
    font-family: "Bebas Neue", sans-serif;
    line-height: 0.76;
  }
  .title__line { display: block; }
  .title__line--copper { color: var(--copper); font-size: 150px; }
  .title__line--lantern { color: var(--teal); font-size: 150px; margin-top: 6px; }
  .title__line--advisory {
    color: var(--ink-light);
    font-size: 66px;
    letter-spacing: 0.02em;
    margin-top: 18px;
  }
  .cover__art {
    position: absolute;
    left: 28px;
    top: 340px;
    width: 460px;
    height: 440px;
    border-radius: 50%;
    background: radial-gradient(circle at 45% 40%, var(--money-gold) 0%, var(--money-green) 45%, rgba(20,20,23,0) 72%);
  }
  .author {
    position: absolute;
    left: 0;
    bottom: 44px;
    width: 100%;
    text-align: center;
    font-family: "Montserrat", sans-serif;
    font-weight: 600;
    font-size: 36px;
    letter-spacing: 0.38em;
    color: var(--ink-light);
  }
</style>
</head>
<body>
  <main class="cover">
    <div class="cover__top"></div>
    <div class="cover__art" role="img" aria-label="Illustration of folded dollar bills forming a broken sphere"></div>
    <h1 class="title">
      <span class="title__line title__line--copper">Copper</span>
      <span class="title__line title__line--lantern">Lantern</span>
      <span class="title__line title__line--advisory">Advisory</span>
    </h1>
    <p class="author">DALE CORVANEK</p>
  </main>
</body>
</html>
```